new service company in the field of construction seeks to make the Creation of a PPT

We need a PPT format with a cover page a frame for presentation. our company is based in Paris which was named VORENTEX. we just did our logo attached. Our company offers services to manage and control documents that pass on projects in construction (building, infrastructure, energy, oil and gas etc. ..). We use internet systems to help us, design must show insurance, quality, and safety. Customers should build any type of works and can not build without the approved documents. These documents go through multiple validations, and vorentex staff seconded on projects, coordinate these processes and documents, quality documents, to ensure that project deadlines are met and project management sees his project developed within the period, through regular reporting. the services offered by our company help ensure the project of building on time, to ensure the project manager visibility on what e will not, and can act accordingly.

Target Market(s)

general contractor of engineering construction or big business masters lumber wholesale real estate investor, project ownership in the construction sector

Industry/Entity Type

Construction

Contact Information for Business Card

carte rectangulaire petite taille (4X6cm env)
horizontale ou verticale
prendre en compte les éléments suivants :
logo
nom de société
adresse postale (4 lignes)
teléphone:
mail
role (ex : directeur)
in the back : La qualité documentaire de vos projets

Font styles to use
Sans Serif

Colors
34a7d7
85cae6
cee9f5
0592cd

Requirements
Must have
• The project should have 2 sliders: slider 1. Cover Page 2. slider for the content of presentations THE GOAL IS TO HAVE A VISUAL IDENTITY ON PPT, MY BUSINESS CARDS AND LETTERS must stay in mind and colors of the logo that joined the design must be clean and recall the seriousness, ease. the design must take into account the page numbers Tag line: the documentary quality of your projects information such as tagline and writes must be modifiable
Nice to have
• would require the presentation of the figure shows concepts or reporting table THE GOAL IS TO HAVE A VISUAL IDENTITY ON PPT, MY BUSINESS CARDS AND LETTERS
Should not have
• not to building or building in the logo

```html
<!DOCTYPE html>
<html lang="en">
<head>
<meta charset="utf-8">
<title>VORENTEX – Presentation Template</title>
<link href="https://fonts.googleapis.com/css2?family=Raleway:wght@300;400;500;600;700&display=swap" rel="stylesheet">
<style>
  :root{
    --brand-blue:#2e75b6;
    --brand-blue-deep:#2a6cab;
    --brand-mid:#6f9bd0;
    --brand-light:#8aadd6;
    --brand-pale:#cddcee;
    --brand-ghost:#e4ecf6;
    --ink:#595959;
    --white:#ffffff;
    --shadow:rgba(0,0,0,.28);
  }
  *{box-sizing:border-box;margin:0;padding:0}
  html,body{width:1200px;height:675px;overflow:hidden;background:var(--white)}
  body{font-family:"Raleway",sans-serif}
  .sheet{
    width:1200px;height:675px;padding:1px 7px;
    display:grid;grid-template-columns:repeat(3,388px);grid-template-rows:repeat(3,219px);
    column-gap:14px;row-gap:8px;
  }
  .slide{position:relative;overflow:hidden;width:388px;height:219px}
  .slide--white{background:var(--white)}
  .slide--blue{background:var(--brand-blue)}
  .slide--light{background:var(--brand-light)}
  .slide svg.backdrop{position:absolute;inset:0;width:100%;height:100%}

  .brand{position:absolute;display:flex;flex-direction:column;align-items:center;gap:3px}
  .brand__dot{width:17px;height:17px;border-radius:50%;background:currentColor}
  .brand__name{font-weight:700;font-size:13px;letter-spacing:.3px;line-height:1}
  .brand--small .brand__dot{width:11px;height:11px}
  .brand--small .brand__name{font-size:9.5px}

  .cover-text{position:absolute}
  .cover-title{font-weight:700;font-size:15px;line-height:1.2;white-space:nowrap}
  .cover-lede{font-size:5.6px;line-height:1.45;margin-top:4px}

  .on-dark{color:var(--white)}
  .on-light{color:var(--brand-blue)}

  .content-title{position:absolute;font-weight:400;font-size:17px;color:var(--brand-blue);white-space:nowrap}
  .content-title--band{color:var(--white)}
  .title-rule{position:absolute;height:1.5px;width:28px;background:var(--brand-blue)}
  .body-copy{position:absolute;left:28px;width:332px;color:var(--ink)}
  .body-copy h3{font-size:8.6px;font-weight:700;color:var(--brand-blue);line-height:1.35;margin-bottom:8px}
  .body-copy p{font-size:6.2px;line-height:1.4;margin-bottom:6px}
  .page-number{position:absolute;font-size:6px;color:var(--ink)}
  .page-chip{position:absolute;width:14px;height:14px;border-radius:50%;background:var(--brand-blue);color:var(--white);font-size:6px;display:flex;align-items:center;justify-content:center}
</style>
</head>
<body>
<main class="sheet">

  <!-- Cover A -->
  <section class="slide slide--white">
    <svg class="backdrop" viewBox="0 0 388 219" role="img" aria-label="Layered blue curved background shapes">
      <circle cx="420" cy="110" r="80" fill="var(--brand-light)"/>
      <circle cx="330" cy="108" r="124" fill="var(--brand-blue)" style="filter:drop-shadow(-6px 6px 6px var(--shadow))"/>
    </svg>
    <div class="brand on-light" style="left:120px;top:68px"><span class="brand__dot"></span><span class="brand__name">VORENTEX</span></div>
    <div class="cover-text on-light" style="left:53px;top:104px;text-align:right;width:132px">
      <div class="cover-title" style="text-align:left">Presentation Title</div>
      <p class="cover-lede" style="color:var(--brand-blue)">Lorem ipsum dolor sit amet, consectetur adipiscing elit, sed do eiusmod tempor incididunt ut labore et dolore magna aliqua.</p>
    </div>
  </section>

  <!-- Cover B -->
  <section class="slide slide--blue">
    <svg class="backdrop" viewBox="0 0 388 219" role="img" aria-label="Soft tonal blue curved background shapes">
      <circle cx="60" cy="100" r="150" fill="var(--brand-mid)" opacity=".35"/>
      <circle cx="150" cy="120" r="90" fill="var(--brand-mid)" opacity=".3"/>
    </svg>
    <div class="brand on-dark" style="left:251px;top:118px"><span class="brand__dot"></span><span class="brand__name">VORENTEX</span></div>
    <div class="cover-text on-dark" style="left:252px;top:156px;width:130px">
      <div class="cover-title">Presentation Title</div>
      <p class="cover-lede">Lorem ipsum dolor sit amet, consectetur adipiscing elit, sed do eiusmod tempor incididunt ut labore et dolore magna aliqua.</p>
    </div>
  </section>

  <!-- Cover C -->
  <section class="slide slide--light">
    <svg class="backdrop" viewBox="0 0 388 219" role="img" aria-label="Pale blue curved background shapes">
      <circle cx="300" cy="110" r="130" fill="var(--white)" opacity=".12"/>
      <circle cx="360" cy="110" r="90" fill="var(--white)" opacity=".12"/>
    </svg>
    <div class="brand on-dark" style="left:90px;top:96px"><span class="brand__dot"></span><span class="brand__name">VORENTEX</span></div>
    <div class="cover-text on-dark" style="left:17px;top:137px;width:152px;text-align:right">
      <div class="cover-title" style="text-align:left">Presentation Title</div>
      <p class="cover-lede">Lorem ipsum dolor sit amet, consectetur adipiscing elit, sed do eiusmod tempor incididunt ut labore et dolore magna aliqua.</p>
    </div>
  </section>

  <!-- Cover D -->
  <section class="slide slide--blue">
    <svg class="backdrop" viewBox="0 0 388 219" role="img" aria-label="Soft tonal blue curved background shapes">
      <circle cx="260" cy="110" r="200" fill="var(--brand-mid)" opacity=".3"/>
      <circle cx="330" cy="110" r="110" fill="var(--brand-mid)" opacity=".3"/>
    </svg>
    <div class="brand on-dark" style="left:158px;top:62px"><span class="brand__dot"></span><span class="brand__name">VORENTEX</span></div>
    <div class="cover-text on-dark" style="left:117px;top:112px;width:160px;text-align:center">
      <div class="cover-title">Presentation Title</div>
      <p class="cover-lede">Lorem ipsum dolor sit amet, consectetur adipiscing elit, sed do eiusmod tempor incididunt ut labore et dolore magna aliqua.</p>
    </div>
  </section>

  <!-- Cover E -->
  <section class="slide slide--blue">
    <svg class="backdrop" viewBox="0 0 388 219" role="img" aria-label="Light blue layered curved shapes">
      <circle cx="190" cy="300" r="150" fill="var(--brand-light)" style="filter:drop-shadow(-4px -3px 5px var(--shadow))"/>
      <circle cx="70" cy="330" r="150" fill="var(--brand-pale)" style="filter:drop-shadow(4px -4px 5px var(--shadow))"/>
    </svg>
    <div class="brand on-dark" style="left:194px;top:42px"><span class="brand__dot"></span><span class="brand__name">VORENTEX</span></div>
    <div class="cover-text on-dark" style="left:198px;top:84px;width:150px">
      <div class="cover-title">Presentation Title</div>
      <p class="cover-lede">Lorem ipsum dolor sit amet, consectetur adipiscing elit, sed do eiusmod tempor incididunt ut labore et dolore magna aliqua.</p>
    </div>
  </section>

  <!-- Cover F -->
  <section class="slide slide--white">
    <svg class="backdrop" viewBox="0 0 388 219" role="img" aria-label="Large pale blue circular background shape">
      <circle cx="190" cy="120" r="130" fill="var(--brand-ghost)" style="filter:drop-shadow(4px 4px 6px rgba(0,0,0,.15))"/>
    </svg>
    <div class="brand on-light" style="left:118px;top:73px"><span class="brand__dot"></span><span class="brand__name">VORENTEX</span></div>
    <div class="cover-text on-light" style="left:119px;top:114px;width:150px">
      <div class="cover-title">Presentation Title</div>
      <p class="cover-lede">Lorem ipsum dolor sit amet, consectetur adipiscing elit, sed do eiusmod tempor incididunt ut labore et dolore magna aliqua.</p>
    </div>
  </section>

  <!-- Content 7 -->
  <section class="slide slide--white">
    <div style="position:absolute;left:0;top:0;width:388px;height:32px;background:var(--brand-blue)"></div>
    <div class="content-title content-title--band" style="left:33px;top:6px">Your Title Goes Here</div>
    <div class="brand brand--small on-dark" style="left:332px;top:4px"><span class="brand__dot"></span><span class="brand__name">VORENTEX</span></div>
    <div class="body-copy" style="top:62px">
      <h3>This is place for your header text. Insert your text here, just replace this text with your own text</h3>
      <p>Lorem ipsum dolor sit amet, consectetur adipiscing elit, sed do eiusmod tempor incididunt ut labore et dolore magna aliqua. Ut enimad minim veniam, quis nostrud exercitation ullamco laboris nisi ut aliquip ex ea commodo consequat.</p>
      <p>Duis aute irure dolor in reprehenderit in voluptate velit esse cillum dolore eu fugiat nulla pariatur. Excepteur sint occaecat cupidatat non proident, sunt inculpa qui officia deserunt mollit anim id est laborum.</p>
      <p>Ut enimad minim veniam, quis nostrud exercitation ullamco laboris nisi ut aliquip ex ea commodo consequat.</p>
    </div>
    <span class="page-number" style="left:367px;top:206px">7</span>
  </section>

  <!-- Content 8 -->
  <section class="slide slide--white">
    <div class="content-title" style="left:108px;top:8px">Your Title Goes Here</div>
    <div class="title-rule" style="left:180px;top:34px"></div>
    <div class="body-copy" style="top:57px">
      <h3>This is place for your header text. Insert your text here, just replace this text with your own text</h3>
      <p>Lorem ipsum dolor sit amet, consectetur adipiscing elit, sed do eiusmod tempor incididunt ut labore et dolore magna aliqua. Ut enimad minim veniam, quis nostrud exercitation ullamco laboris nisi ut aliquip ex ea commodo consequat.</p>
      <p>Duis aute irure dolor in reprehenderit in voluptate velit esse cillum dolore eu fugiat nulla pariatur. Excepteur sint occaecat cupidatat non proident, sunt inculpa qui officia deserunt mollit anim id est laborum.</p>
      <p>Ut enimad minim veniam, quis nostrud exercitation ullamco laboris nisi ut aliquip ex ea commodo consequat.</p>
    </div>
    <div class="brand brand--small on-light" style="left:3px;top:194px"><span class="brand__dot"></span><span class="brand__name">VORENTEX</span></div>
    <div style="position:absolute;left:0;bottom:0;width:388px;height:3px;background:var(--brand-blue)"></div>
    <span class="page-chip" style="left:361px;top:198px">8</span>
  </section>

  <!-- Content 9 -->
  <section class="slide slide--white">
    <svg class="backdrop" viewBox="0 0 388 219" role="img" aria-label="Pale blue curved decorative shape">
      <circle cx="350" cy="175" r="90" fill="var(--brand-pale)" opacity=".75"/>
    </svg>
    <div class="content-title" style="left:20px;top:8px">Your Title Goes Here</div>
    <div class="title-rule" style="left:22px;top:34px"></div>
    <div class="brand brand--small on-light" style="left:334px;top:12px"><span class="brand__dot"></span><span class="brand__name">VORENTEX</span></div>
    <div style="position:absolute;left:0;bottom:0;width:388px;height:11px;background:var(--brand-blue)"></div>
    <span class="page-number" style="left:6px;top:209px;color:var(--white);font-size:4.5px">© 2017 VORENTEX. All rights reserved</span>
    <span class="page-number" style="left:369px;top:208px;background:var(--white);color:var(--ink);padding:0 2px">9</span>
  </section>

</main>
</body>
</html>
```